Kelvo Tech Oz Business card revamp

We are looking to revamp our business card design. We are hoping to change our colours to dark navey blue, gray, white and black but are open to keeping the same if a good design is submited. We are after somthing a bit differnt not just boring business card. I have attached a copy of our current card. We Want to keep the same logo design which i have attached a few to hopfully help you in this process. We are after a design that can be personalized to separate 4 people

Colors
0455a3
ffffff
000000
cbcbcb

Requirements
Must have
• Kelvo Tech Logo, address 3/41 Mallory Court, Wexhill 4218, phone number, Name and position

```html
<!DOCTYPE html>
<html lang="en">
<head>
<meta charset="utf-8">
<title>Kelvo Tech – Business Card</title>
<link href="https://fonts.googleapis.com/css2?family=Arimo:wght@400;700&display=swap" rel="stylesheet">
<style>
  :root {
    --brand-blue: #1170b8;
    --brand-blue-deep: #0a62a8;
    --accent-orange: #e8731e;
    --text-grey: #666666;
    --rule-grey: #8a8a8a;
    --card-white: #ffffff;
    --backdrop: #e9e9ea;
  }
  * { margin: 0; padding: 0; box-sizing: border-box; }
  html, body {
    width: 1200px; height: 800px; overflow: hidden;
    background: var(--backdrop);
    font-family: "Arimo", Arial, sans-serif;
  }
  .stage {
    position: relative; width: 1200px; height: 800px;
    display: flex; align-items: center; justify-content: center; gap: 50px;
  }
  .card {
    position: relative; width: 525px; height: 300px;
    box-shadow: 0 6px 18px rgba(0,0,0,0.12);
  }
  /* Front */
  .card-front { background: var(--card-white); }
  .front-brand {
    position: absolute; right: 48px; top: 62px; text-align: right;
  }
  .brand-mark {
    display: flex; align-items: center; justify-content: flex-end; gap: 10px;
  }
  .brand-dot {
    width: 26px; height: 26px; border-radius: 50%; background: var(--accent-orange);
  }
  .brand-name {
    font-weight: 700; font-size: 34px; letter-spacing: -0.5px; color: var(--brand-blue);
  }
  .brand-tagline {
    margin-top: 2px; font-weight: 700; font-size: 12.5px; color: var(--brand-blue);
    letter-spacing: 0.3px;
  }
  .holder {
    position: absolute; left: 50px; top: 142px;
  }
  .holder-name {
    font-weight: 700; font-size: 20px; color: var(--accent-orange);
  }
  .holder-role {
    margin-top: 1px; font-size: 15px; color: var(--text-grey);
  }
  .divider {
    position: absolute; left: 50px; right: 60px; top: 198px;
    border-top: 1px solid var(--rule-grey);
  }
  .contact {
    position: absolute; left: 50px; top: 214px; list-style: none;
    font-size: 15px; color: var(--text-grey); line-height: 21px;
  }
  .contact li { display: flex; align-items: flex-start; gap: 10px; }
  .contact svg { width: 13px; height: 13px; margin-top: 4px; flex: none; }
  .contact .indent { padding-left: 23px; }
  /* Back */
  .card-back {
    background: linear-gradient(160deg, var(--brand-blue) 0%, var(--brand-blue-deep) 100%);
    display: flex; flex-direction: column; align-items: center; justify-content: center;
    color: var(--card-white);
  }
  .back-brand { display: flex; align-items: center; gap: 12px; }
  .back-brand .brand-dot { background: var(--card-white); width: 30px; height: 30px; }
  .back-brand .brand-name { color: var(--card-white); font-size: 44px; }
  .back-tagline {
    margin-top: 4px; font-weight: 700; font-size: 16px; letter-spacing: 0.4px;
  }
  .web {
    margin-top: 26px; font-size: 14px; letter-spacing: 1.5px; opacity: 0.9;
  }
</style>
</head>
<body>
  <main class="stage">
    <section class="card card-front" aria-label="Card front">
      <div class="front-brand">
        <div class="brand-mark">
          <span class="brand-dot"></span>
          <span class="brand-name">Kelvo Tech</span>
        </div>
        <p class="brand-tagline">Passive Fire Protection</p>
      </div>
      <div class="holder">
        <h1 class="holder-name">Daniel Hartley</h1>
        <p class="holder-role">Managing Director</p>
      </div>
      <div class="divider"></div>
      <ul class="contact">
        <li>
          <svg viewBox="0 0 24 24" aria-hidden="true"><path fill="#e8731e" d="M6.6 10.8a15 15 0 0 0 6.6 6.6l2.2-2.2a1 1 0 0 1 1-.25 11.4 11.4 0 0 0 3.6.57 1 1 0 0 1 1 1V20a1 1 0 0 1-1 1A17 17 0 0 1 3 4a1 1 0 0 1 1-1h3.5a1 1 0 0 1 1 1c0 1.25.2 2.45.57 3.57a1 1 0 0 1-.25 1z"/></svg>
          <span>(+61) 07 4821 3904</span>
        </li>
        <li>
          <svg viewBox="0 0 24 24" aria-hidden="true"><path fill="#e8731e" d="M12 2a7 7 0 0 0-7 7c0 5.25 7 13 7 13s7-7.75 7-13a7 7 0 0 0-7-7zm0 9.5A2.5 2.5 0 1 1 12 6.5a2.5 2.5 0 0 1 0 5z"/></svg>
          <span>3/41 Mallory Court</span>
        </li>
        <li class="indent">Wexhill 4218</li>
      </ul>
    </section>

    <section class="card card-back" aria-label="Card back">
      <div class="back-brand">
        <span class="brand-dot"></span>
        <span class="brand-name">Kelvo Tech</span>
      </div>
      <p class="back-tagline">Passive Fire Protection</p>
      <p class="web">www.kelvotech.com.au</p>
    </section>
  </main>
</body>
</html>
```